Criação de Apres. Comercial (com dobra) para Construção & Engenharia
" Pessoal, vocês verão em documento em anexo que é a versão da nossa página WEB que está em construção que oferecemos serviços de: 1- Reforma & Construção * Projeto Guia de Reforma Fornecemos a planta com alterações e novas medidas. * Orçamento Enviamos nossa proposta de orçamento totalmente grátis. * Acompanhamento de Engenheiro Civil e Arquiteto* Equipe de profissionais capacitados. * Cotação de melhores preços de materiais; Auxiliamos na busca de melhores preços e condições de pagamento para a sua casa plena ou obra. * Seleção de parceiros para execução; Selecionamos profissionais capacitados para a execução da sua casa plena ou obra. 1.1 Assessoria * Acompanhamos o projeto em execução Acompanhamento das atividades associadas ao planejamento, organização, direção e controle necessários para garantir o sucesso da sua casa plena ou obra. * Programação da Obra Compreendendo o detalhamento dos serviços e as providências preliminares, a programação dos materiais, mão de obra e equipamentos. * Relatórios de Andamento da obra Adequação do projeto e da construção às necessidades do cliente no que se refere à qualidade, prazo e custo. 2- Além disso temos a opção:" sua casa plena protegida": * Substituição de materiais danificados Qualquer material danificado por nossos profissionais ou fornecedores são repostos na mesma qualidade e quantidade, sem custos para o cliente. * Correção dos serviços mal executados* Mesmo buscando fornecer o resultado que você espera e sempre trabalhando com profissionais capacitados, erros podem acontecer. Diante disso, asseguramos a conclusão da sua obra com qualidade. * Troca de fornecedor Selecionamos os melhores profissionais do mercado. Mesmo assim, se você não gostar, é livre para nos solicitar a troca. 3- Temos também: "Tudo melhor para você" * Orçamento gratuito * Gestão de pagamento * Prazo e rapidez * Saiba tudo que está acontecendo na sua casa plena * Garantia de Satisfação * Consultoria Técnica * Cronograma de gerenciamento * Otimização de custos * Equipe preparada 4- ORÇAMENTO Vocês verão no documento em anexo que trabalhamos muito com a opção de ORÇAMENTO GRÁTIS. Não se esqueçam de citar isso em nessa apresentação. 5- SEJA NOSSO PARCEIRO Caso sobre espaço no preenchimento do conteúdo. Pode-se aproveitar o campo para PARCEIROS (A empresa trabalha com parceiros/ fornecedores que executam a obra). Pode utilizar o campo orientando o parceiro para entrar no site e se cadastrar. Imagens em anexo irão auxiliá-los. 6-Somos uma empresa NOVA, então não temos nenhum projeto realizado até o momento. OBS IMPORTANTE: - Façam o uso de imagens modernas e suaves.. Queremos ser diferentes e inovadores e precisamos muito da criatividade de vocês. "

```html
<!DOCTYPE html>
<html lang="pt-BR">
<head>
<meta charset="utf-8">
<title>casa plena – pasta comercial</title>
<link href="https://fonts.googleapis.com/css2?family=Raleway:wght@300;400;500&display=swap" rel="stylesheet">
<style>
  :root {
    --stage: #e8e9eb;
    --blue: #1f5fae;
    --blue-deep: #154a91;
    --blue-light: #3f7fc8;
    --sky: #6aa8e6;
    --white: #ffffff;
    --ink-soft: #cfe0f4;
    --photo-a: #eef1f4;
    --photo-b: #c9d2dc;
    --photo-c: #8f9eae;
  }
  * { box-sizing: border-box; margin: 0; padding: 0; }
  html, body { width: 1200px; height: 1200px; overflow: hidden; }
  body {
    background: var(--stage);
    font-family: "Raleway", Arial, sans-serif;
    position: relative;
  }
  .folder-spread {
    position: absolute;
    left: 40px; top: 204px;
    width: 1120px; height: 792px;
    display: flex;
    box-shadow: 0 6px 24px rgba(0,0,0,.12);
  }
  .page { position: relative; width: 560px; height: 792px; overflow: hidden; }

  /* back cover */
  .back-cover {
    background: linear-gradient(160deg, var(--blue-light) 0%, var(--blue) 45%, var(--blue-deep) 100%);
  }
  .back-brand {
    position: absolute; left: 64px; top: 560px;
    display: flex; align-items: center; gap: 14px;
  }
  .brand-square { width: 30px; height: 30px; background: var(--white); }
  .back-brand .brand-name {
    color: var(--white); font-weight: 300; font-size: 32px; letter-spacing: .5px; line-height: 1;
  }
  .back-tagline {
    position: absolute; left: 108px; top: 598px;
    color: var(--ink-soft); font-size: 8px; letter-spacing: 2.6px; text-transform: uppercase;
  }
  .contact-list {
    position: absolute; left: 66px; top: 636px; list-style: none;
  }
  .contact-list li {
    display: flex; align-items: center; gap: 10px;
    color: var(--ink-soft); font-size: 10px; line-height: 20px;
  }
  .contact-list svg { width: 10px; height: 10px; fill: var(--ink-soft); }

  /* front cover */
  .front-cover { background: var(--white); }
  .front-brand {
    position: absolute; left: 0; right: 0; top: 96px;
    display: flex; flex-direction: column; align-items: center;
  }
  .front-brand .brand-square { width: 48px; height: 48px; background: var(--blue); margin-bottom: 16px; }
  .front-brand .brand-name {
    color: var(--blue); font-weight: 300; font-size: 44px; letter-spacing: .5px; line-height: 1;
  }
  .front-tagline {
    margin-top: 10px; color: var(--blue); font-size: 9px; letter-spacing: 3px; text-transform: uppercase;
  }
  .interior-photo {
    position: absolute; left: 0; right: 0; top: 330px; height: 370px;
    background: linear-gradient(180deg, var(--photo-a) 0%, var(--photo-b) 60%, var(--photo-c) 100%);
    border-top: 6px solid var(--sky);
  }
  .url-band {
    position: absolute; left: 0; right: 0; bottom: 0; height: 92px;
    background: var(--blue);
    display: flex; align-items: center; justify-content: flex-end; padding-right: 48px;
  }
  .url-band span { color: var(--white); font-size: 22px; font-weight: 400; letter-spacing: .5px; }
</style>
</head>
<body>
  <div class="folder-spread">
    <section class="page back-cover">
      <div class="back-brand">
        <span class="brand-square"></span>
        <span class="brand-name">casa plena</span>
      </div>
      <p class="back-tagline">Reforma, construção e assessoria</p>
      <ul class="contact-list">
        <li><svg viewBox="0 0 10 10"><path d="M2 0h2l1 2.5-1.3 1a6 6 0 0 0 2.8 2.8l1-1.3L10 6v2a2 2 0 0 1-2 2A8 8 0 0 1 0 2a2 2 0 0 1 2-2z"/></svg>+55 11 4000-2100</li>
        <li><svg viewBox="0 0 10 10"><path d="M3 0h4a1 1 0 0 1 1 1v8a1 1 0 0 1-1 1H3a1 1 0 0 1-1-1V1a1 1 0 0 1 1-1zm0 1.5v6h4v-6z"/></svg>+55 11 98000-2100</li>
        <li><svg viewBox="0 0 10 10"><path d="M0 2h10v6H0zm1 1v.3l4 2.5 4-2.5V3z"/></svg>contato@casaplena.com.br</li>
        <li><svg viewBox="0 0 10 10"><path d="M5 0a3.5 3.5 0 0 1 3.5 3.5C8.5 6 5 10 5 10S1.5 6 1.5 3.5A3.5 3.5 0 0 1 5 0zm0 2a1.5 1.5 0 1 0 0 3 1.5 1.5 0 0 0 0-3z"/></svg>Av. das Palmeiras, 321, Vila Nova/SP</li>
      </ul>
    </section>

    <section class="page front-cover">
      <div class="front-brand">
        <span class="brand-square"></span>
        <span class="brand-name">casa plena</span>
        <p class="front-tagline">Reforma, construção e assessoria</p>
      </div>
      <div class="interior-photo" role="img" aria-label="Fotografia de uma sala de estar moderna e clara, recém-reformada, com sofá branco e piso de madeira"></div>
      <div class="url-band"><span>www.casaplena.com.br</span></div>
    </section>
  </div>
</body>
</html>
```